SilverLedgerOak - Double Sided Business Card

We are looking for design options or our business cards. We are a Business Solutions and HR solutions Provider - the theme is business, for this card.

Our brand colours are represented within our logo.

Details needed to be put on the front of the business card are:

Employees name: [Sample Name]
Role: [Sample Role]

Address: Suite 4 - Level 3/48 Halloran Avenue Parramatta NSW 2150
M: 0000 000 000
P: 1300 847 213
F: 1300 847 286
E: sample@silverledgeroak.com.au
www.silverledgeroak.com.au
Updates

Reason: Hello, could we please increase our deadline by 5 days. Thanking you, Tess

Target Market(s)

Business Owners, also Candidates looking for Employment

Industry/Entity Type

Business

Contact Information for Business Card

Role: [Sample Role]

M: 0000 000 000
P: 1300 847 213
F: 1300 847 286

Font styles to use
Sans Serif

Colors
3276b5
3176b5
0455a3
85abd2
cfdeed
ffffff
000000
1b1b1b
757575

Requirements
Must have
• Details needed to be put on the front of the business card are:
• Employees name: [Sample Name]
• Role: [Sample Role]
• Address: Suite 4 - Level 3/48 Halloran Avenue Parramatta NSW 2150
• M: 0000 000 000
• P: 1300 847 213
• F: 1300 847 286
• E: sample@silverledgeroak.com.au
• www.silverledgeroak.com.au
Nice to have
• Simplicity, clean and professional.

```html
<!DOCTYPE html>
<html lang="en">
<head>
<meta charset="utf-8">
<title>SilverLedgerOak Business Card</title>
<link rel="stylesheet" href="https://fonts.googleapis.com/css2?family=Roboto:wght@400;500;700;900&family=Roboto+Condensed:wght@500;700&display=swap">
<style>
  :root {
    --backdrop: #e4e4e4;
    --card-white: #f4f4f4;
    --brand-blue: #0d57a6;
    --brand-mid: #0455a3;
    --navy: #102a4a;
    --ink: #1b1b1b;
    --muted: #4a4a4a;
    --rule: #c9c9c9;
    --white: #ffffff;
  }
  * { box-sizing: border-box; margin: 0; padding: 0; }
  html, body { width: 1200px; height: 960px; overflow: hidden; }
  body { background: var(--backdrop); font-family: "Roboto", Arial, sans-serif; position: relative; }

  .card { position: absolute; width: 600px; height: 343px; box-shadow: 0 2px 4px rgba(0,0,0,.25); overflow: hidden; }
  .card-front { left: 314px; top: 113px; background: var(--card-white); }
  .card-back { left: 311px; top: 472px; background: var(--brand-blue); }

  .brand { position: absolute; text-align: center; }
  .brand-mark { display: block; margin: 0 auto 10px; width: 72px; height: 72px; }
  .brand-name { font-weight: 900; font-size: 24px; letter-spacing: .2px; line-height: 1; }
  .brand-tagline { font-weight: 700; font-size: 8.6px; margin-top: 12px; white-space: nowrap; }

  .card-front .brand { left: 40px; top: 110px; width: 236px; }
  .card-front .brand-mark { background: var(--brand-mid); }
  .card-front .brand-name { color: var(--brand-mid); }
  .card-front .brand-tagline { color: var(--ink); }

  .divider { position: absolute; left: 291px; top: 62px; width: 1px; height: 222px; background: var(--rule); }

  .details { position: absolute; left: 312px; top: 62px; }
  .person-name { font-family: "Roboto Condensed", Arial, sans-serif; font-weight: 700; font-size: 20px; color: var(--navy); line-height: 24px; }
  .person-role { font-family: "Roboto Condensed", Arial, sans-serif; font-weight: 500; font-size: 15px; color: var(--brand-mid); line-height: 20px; margin-top: 2px; }
  .address { font-size: 14.5px; color: var(--muted); line-height: 18px; margin-top: 13px; }
  .contact-list { list-style: none; margin-top: 5px; }
  .contact-list li { display: flex; align-items: center; font-size: 14.5px; color: var(--muted); line-height: 19.2px; }
  .contact-list svg { width: 12px; height: 12px; margin-right: 11px; fill: var(--navy); flex: none; }

  .footer-band { position: absolute; left: 0; bottom: 0; width: 600px; height: 23px; }

  .card-back .brand { left: 0; top: 72px; width: 600px; }
  .card-back .brand-mark { background: var(--white); width: 100px; height: 100px; margin-bottom: 16px; }
  .card-back .brand-name { color: var(--white); font-size: 30px; }
  .card-back .brand-tagline { color: var(--white); font-size: 10px; margin-top: 20px; }
  .back-web { position: absolute; left: 0; top: 300px; width: 600px; text-align: center; color: var(--white); font-size: 14px; letter-spacing: 2.2px; }
</style>
</head>
<body>
  <section class="card card-front">
    <div class="brand">
      <span class="brand-mark"></span>
      <div class="brand-name">SilverLedgerOak</div>
      <div class="brand-tagline">Practical people and business solutions for growing teams</div>
    </div>
    <div class="divider"></div>
    <div class="details">
      <div class="person-name">MARK ELLISON</div>
      <div class="person-role">CEO/FOUNDER</div>
      <p class="address">Suite 4 - Level 3/48<br>Halloran Avenue<br>Parramatta NSW 2150</p>
      <ul class="contact-list">
        <li><svg viewBox="0 0 24 24"><path d="M6.6 10.8a15.1 15.1 0 0 0 6.6 6.6l2.2-2.2c.3-.3.7-.4 1-.2 1.1.4 2.3.6 3.6.6.6 0 1 .4 1 1V20c0 .6-.4 1-1 1A17 17 0 0 1 3 4c0-.6.4-1 1-1h3.5c.6 0 1 .4 1 1 0 1.3.2 2.5.6 3.6.1.3 0 .7-.2 1z"/></svg>1300 847 213</li>
        <li><svg viewBox="0 0 24 24"><path d="M7 1h10a2 2 0 0 1 2 2v18a2 2 0 0 1-2 2H7a2 2 0 0 1-2-2V3a2 2 0 0 1 2-2zm0 3v14h10V4zm5 15.2a1.2 1.2 0 1 0 0 2.4 1.2 1.2 0 0 0 0-2.4z"/></svg>0000 000 000</li>
        <li><svg viewBox="0 0 24 24"><path d="M6 2h12v6H6zM3 9h18a2 2 0 0 1 2 2v7h-4v4H5v-4H1v-7a2 2 0 0 1 2-2zm4 7v4h10v-4z"/></svg>1300 847 286</li>
        <li><svg viewBox="0 0 24 24"><path d="M2 5h20v14H2zm2 2v.5l8 5 8-5V7z"/></svg>sample@silverledgeroak.com.au</li>
        <li><svg viewBox="0 0 24 24"><path d="M12 2a10 10 0 1 0 0 20 10 10 0 0 0 0-20zm-1 17.9A8 8 0 0 1 4.2 9.8L9 14.6v1a2 2 0 0 0 2 2zm6.9-2.5a2 2 0 0 0-1.9-1.4h-1v-3a1 1 0 0 0-1-1H8v-2h2a1 1 0 0 0 1-1V7h2a2 2 0 0 0 2-2v-.4a8 8 0 0 1 2.9 12.8z"/></svg>www.silverledgeroak.com.au</li>
      </ul>
    </div>
    <svg class="footer-band" viewBox="0 0 600 23" preserveAspectRatio="none" aria-hidden="true">
      <polygon points="0,0 393,0 388,23 0,23" fill="#102a4a"/>
      <polygon points="397,0 600,0 600,23 392,23" fill="#0d57a6"/>
    </svg>
  </section>

  <section class="card card-back">
    <div class="brand">
      <span class="brand-mark"></span>
      <div class="brand-name">SilverLedgerOak</div>
      <div class="brand-tagline">Practical people and business solutions for growing teams</div>
    </div>
    <div class="back-web">www.silverledgeroak.com.au</div>
  </section>
</body>
</html>
```